Letterhead and Business Cards

Using our new logo we would like designs for the following,

1.Letterhead

2. 2 x Business Cards

I will need all three in high quality PDF files ready for printing. I will also require the top and bottom of the letterhead as two JPG files.

Target Market(s)

We are a business to business company dealing with middle to upper management both as clients and suppliers.

Industry/Entity Type

Business

Requirements
Must have
• 1. Look professional.
• 2. Utilise our logo colours
• 3. Incorporate our logo on both.
• 4. Letterhead

• Address:
• Pell Harrow Court
• Pell Harrow Lane
• London
• WC1R 4JZ

• Tel:0845 312 4096
• Fax: 0845 312 7158
• Website: www.kovimerlox.com
• Email: info@kovimerlox.com

• Directors: D.R. Marsh and H.J. Marsh Company Registration No: 52064918(This should be quite small in the letterhead footer somewhere)

• Business Card One Sided Only

• 1. Dominic R. Marsh
• Managing Director

• Address:
• Pell Harrow Court
• Pell Harrow Lane
• London
• WC1R 4JZ

• Tel:0845 312 4096
• Fax: 0845 312 7159
• Mob: 0791 526 3307
• Email: dominic@kovimerlox.com

• 2. Helen J. Marsh
• Sales Director

• Address:
• Pell Harrow Court
• Pell Harrow Lane
• London
• WC1R 4JZ

• Tel:0845 312 4096
• Fax: 0845 312 7158
• Mob: 0794 862 1190
• Email: helen@kovimerlox.com

• Please note some of this info may change for final printing.

```html
<!DOCTYPE html>
<html lang="en">
<head>
<meta charset="utf-8">
<title>Kovimerlox – Letterhead and Business Cards</title>
<link rel="stylesheet" href="https://fonts.googleapis.com/css2?family=Roboto:ital,wght@0,400;0,700;1,400&display=swap">
<style>
  :root {
    --green-dark: #4ea243;
    --green: #5aab42;
    --green-light: #7dbd3e;
    --green-pale: #c8e0a8;
    --label-green: #8cc63f;
    --card-label: #b5dc82;
    --grey: #8a8a8a;
    --grey-text: #6f6f6f;
    --grey-line: #d9d9d9;
    --white: #ffffff;
  }
  * { box-sizing: border-box; margin: 0; padding: 0; }
  html, body { width: 1018px; height: 1200px; overflow: hidden; background: var(--white); }
  body { position: relative; font-family: "Roboto", Arial, sans-serif; }

  .letterhead {
    position: absolute; left: 66px; top: 102px; width: 715px; height: 1012px;
    background: var(--white); box-shadow: 0 1px 5px rgba(0,0,0,.28); overflow: hidden;
  }
  .letterhead__topband { position: absolute; left: 0; top: 0; width: 715px; height: 40px; }
  .brand { position: absolute; display: flex; align-items: center; gap: 8px;
    font-weight: 700; color: var(--green); letter-spacing: -.5px; }
  .brand__dot { border-radius: 50%; background: var(--green); }
  .letterhead .brand { left: 20px; top: 108px; font-size: 38px; }
  .letterhead .brand__dot { width: 26px; height: 26px; }

  .address-block { position: absolute; text-align: right; font-style: italic; color: var(--grey-text); }
  .address-block .label { color: var(--label-green); }
  .letterhead .address-block { right: 31px; top: 36px; font-size: 10.5px; line-height: 12.1px; }
  .letterhead .address-block .gap { height: 12px; }
  .letterhead__bar { position: absolute; left: 692px; top: 38px; width: 6px; height: 106px; background: var(--grey); }
  .letterhead__rule { position: absolute; left: 0; top: 159px; width: 696px; height: 6px;
    background: linear-gradient(90deg, #eef6e4, var(--green-pale)); }
  .letterhead__rule-grey { position: absolute; left: 0; top: 169px; width: 696px; height: 2px; background: var(--grey-line); }

  .letterhead__footer { position: absolute; left: 0; top: 812px; width: 715px; height: 200px; }
  .footer-contacts { position: absolute; left: 16px; top: 966px; display: flex; gap: 16px;
    font-size: 10.5px; font-style: italic; color: var(--white); }
  .footer-contacts li { list-style: none; display: flex; align-items: center; gap: 5px; }
  .footer-contacts li::before { content: ""; width: 7px; height: 7px; background: var(--label-green); }
  .footer-contacts .label { color: var(--card-label); }
  .footer-legal { position: absolute; right: 18px; top: 998px; font-size: 6.6px; color: var(--white); }

  .card { position: absolute; left: 650px; width: 289px; height: 185px; background: var(--white);
    box-shadow: 0 1px 4px rgba(0,0,0,.3); overflow: hidden; }
  .card--dominic { top: 320px; }
  .card--helen { top: 531px; }
  .card__wave { position: absolute; left: 0; top: 0; width: 289px; height: 185px; }
  .card .brand { left: 8px; top: 46px; font-size: 18px; gap: 5px; }
  .card .brand__dot { width: 13px; height: 13px; }
  .card .address-block { right: 12px; top: 4px; font-size: 9px; line-height: 11px; }
  .card__bar { position: absolute; left: 280px; top: 6px; width: 5px; height: 40px; background: var(--grey); }
  .card__name { position: absolute; left: 8px; top: 91px; font-size: 15px; font-weight: 700; color: var(--white); }
  .card__title { position: absolute; left: 8px; top: 108px; font-size: 10px; color: var(--white); }
  .card__rule { position: absolute; left: 8px; top: 121px; width: 179px; height: 2px; background: var(--label-green); }
  .card .contact-block { right: 12px; top: 120px; font-size: 9px; line-height: 11.4px; color: var(--white); }
  .card .contact-block .label { color: var(--card-label); }
  .card__sidebar { position: absolute; left: 280px; top: 122px; width: 4px; height: 54px; background: var(--label-green); }
  .card__base { position: absolute; left: 0; top: 179px; width: 289px; height: 6px; background: #a9a9a9; }
</style>
</head>
<body>

<section class="letterhead" aria-label="Letterhead">
  <svg class="letterhead__topband" viewBox="0 0 715 40" aria-hidden="true">
    <defs>
      <linearGradient id="topGrad" x1="0" x2="1">
        <stop offset="0" stop-color="#4ea243"/><stop offset="1" stop-color="#8cc63f"/>
      </linearGradient>
    </defs>
    <path d="M240 10 Q300 22 345 29" fill="none" stroke="#999" stroke-width="1.6" stroke-dasharray="1.5 2.5"/>
    <path d="M222 10 L698 10 L698 20 Q660 30 560 30 L420 30 Q330 28 222 10 Z" fill="url(#topGrad)"/>
    <path d="M270 10 Q320 14 350 30 L365 30 Q330 16 300 10 Z" fill="#fff"/>
    <path d="M640 30 Q680 22 698 14" fill="none" stroke="#fff" stroke-width="3"/>
    <path d="M680 28 Q692 25 698 22" fill="none" stroke="#999" stroke-width="1.6" stroke-dasharray="1.5 2.5"/>
  </svg>

  <div class="brand"><span class="brand__dot"></span>Kovimerlox</div>

  <address class="address-block">
    Pell Harrow Court<br>Pell Harrow Lane<br>London<br>WC1R 4JZ
    <div class="gap"></div>
    <span class="label">Tel:</span> 0845 312 4096<br>
    <span class="label">Fax:</span> 0845 312 7158<br>
    <span class="label">Website:</span> www.kovimerlox.com<br>
    <span class="label">Email:</span> info@kovimerlox.com
  </address>
  <div class="letterhead__bar"></div>
  <div class="letterhead__rule"></div>
  <div class="letterhead__rule-grey"></div>

  <svg class="letterhead__footer" viewBox="0 0 715 200" aria-hidden="true">
    <defs>
      <linearGradient id="footGrad" x1="0" x2="1">
        <stop offset="0" stop-color="#4ea243"/><stop offset="1" stop-color="#6fb540"/>
      </linearGradient>
    </defs>
    <path d="M0 116 C120 92 220 88 330 104 S600 158 715 156" fill="none" stroke="#888" stroke-width="1.8" stroke-dasharray="1.5 2.6"/>
    <path d="M0 124 C120 102 220 100 330 114 S600 166 715 164" fill="none" stroke="#5aab42" stroke-width="3.5"/>
    <path d="M0 131 C120 110 220 108 330 122 S600 174 715 172 L715 200 L0 200 Z" fill="url(#footGrad)"/>
    <rect x="0" y="180" width="715" height="3" fill="#8cc63f" opacity=".7"/>
  </svg>

  <ul class="footer-contacts">
    <li><span><span class="label">T:</span> 0845 312 4096</span></li>
    <li><span><span class="label">W:</span> www.kovimerlox.com</span></li>
    <li><span><span class="label">E:</span> info@kovimerlox.com</span></li>
  </ul>
  <p class="footer-legal">Directors: D.R. Marsh and H.J. Marsh Company Registration No: 52064918</p>
</section>

<section class="card card--dominic" aria-label="Business card, Dominic R. Marsh">
  <svg class="card__wave" viewBox="0 0 289 185" aria-hidden="true">
    <path d="M0 80 C80 82 150 70 200 58 S265 50 289 52" fill="none" stroke="#999" stroke-width="1.2" stroke-dasharray="1 2"/>
    <path d="M0 84 C80 86 150 74 200 62 S265 54 289 56" fill="none" stroke="#5aab42" stroke-width="2.5"/>
    <path d="M0 88 C80 90 150 78 200 66 S265 58 289 60 L289 185 L0 185 Z" fill="#5aab42"/>
  </svg>
  <div class="brand"><span class="brand__dot"></span>Kovimerlox</div>
  <address class="address-block">Pell Harrow Court<br>Pell Harrow Lane<br>London<br>WC1R 4JZ</address>
  <div class="card__bar"></div>
  <h2 class="card__name">Dominic R. Marsh</h2>
  <p class="card__title">Managing Director</p>
  <div class="card__rule"></div>
  <address class="address-block contact-block">
    <span class="label">Tel:</span> 0845 312 4096<br>
    <span class="label">Fax:</span> 0845 312 7159<br>
    <span class="label">Mob:</span> 0791 526 3307<br>
    <span class="label">Website:</span> www.kovimerlox.com<br>
    <span class="label">Email:</span> dominic@kovimerlox.com
  </address>
  <div class="card__sidebar"></div>
  <div class="card__base"></div>
</section>

<section class="card card--helen" aria-label="Business card, Helen J. Marsh">
  <svg class="card__wave" viewBox="0 0 289 185" aria-hidden="true">
    <path d="M0 80 C80 82 150 70 200 58 S265 50 289 52" fill="none" stroke="#999" stroke-width="1.2" stroke-dasharray="1 2"/>
    <path d="M0 84 C80 86 150 74 200 62 S265 54 289 56" fill="none" stroke="#5aab42" stroke-width="2.5"/>
    <path d="M0 88 C80 90 150 78 200 66 S265 58 289 60 L289 185 L0 185 Z" fill="#5aab42"/>
  </svg>
  <div class="brand"><span class="brand__dot"></span>Kovimerlox</div>
  <address class="address-block">Pell Harrow Court<br>Pell Harrow Lane<br>London<br>WC1R 4JZ</address>
  <div class="card__bar"></div>
  <h2 class="card__name">Helen J. Marsh</h2>
  <p class="card__title">Sales Director</p>
  <div class="card__rule"></div>
  <address class="address-block contact-block">
    <span class="label">Tel:</span> 0845 312 4096<br>
    <span class="label">Fax:</span> 0845 312 7158<br>
    <span class="label">Mob:</span> 0794 862 1190<br>
    <span class="label">Website:</span> www.kovimerlox.com<br>
    <span class="label">Email:</span> helen@kovimerlox.com
  </address>
  <div class="card__sidebar"></div>
  <div class="card__base"></div>
</section>

</body>
</html>
```